Corporate Profile
Advisory Services Firm
The main purpose of this marketing collateral is to provide a document that sales staff can leave with customers after an appointment.
Corporate Services
Senior executives. A typical reader of this material will be in a decision making role within a large organisation (more than 500 employees).
Maximum eight pages (including front and rear cover.
Consistent in theme and style with the Amber Fern website
Sections to include:
Front cover (quirky and interesting, perhaps also using the ‘tree and grass’ image from the website
Company profile (who we are and what we do, using the values from the website- single page
Advisory services (six key areas, from the website) – double page
Making a difference (selected success stories and customer quotes) – double page spread
Tallyforge Suite (product overview and list of frameworks) – double page spread
Amber Fern in the community (using information from the website) – single page
Back page (contact details, website details, what else?)
FORMAT
Finished product to be provided in Adobe InDesign CS5 file format, although proofs can be delivered as PDF files.
Primary colour palette is
TS Green
C 50
M 0
Y 85
B 0
TS Grey
M 40
Y 40
B 20
TS Blue (complementary, not main)
C 73.79
M 55.26
Y 16.58
B 1.22
SUPPORTING INFORMATION PROVIDED
Amber Fern website address: www.amberfern-studio.com.au
Tallyforge Suite website mockups: please request from morwenk@amberfern-studio.com.au
Sample page showing required information on the Tallyforge Suite spread. Taken from various pages on www.tallyforgesuite.com.au:8081/

```html
<!DOCTYPE html>
<html lang="en">
<head>
<meta charset="utf-8">
<title>Amber Fern – Corporate Profile Spread</title>
<link rel="stylesheet" href="https://fonts.googleapis.com/css2?family=Open+Sans:wght@400;600;700;800&family=Great+Vibes&display=swap">
<style>
  :root {
    --ts-green: #8cc63f;
    --ts-green-dark: #6aa82e;
    --ts-blue: #1e8fd0;
    --ts-blue-deep: #4a6fa8;
    --ts-grey: #8f7d73;
    --ink: #4d4d4d;
    --paper: #ffffff;
    --gutter: #e6e6e6;
  }
  * { box-sizing: border-box; margin: 0; padding: 0; }
  html, body { width: 1200px; height: 799px; overflow: hidden; background: var(--gutter); }
  body { font-family: "Open Sans", Arial, sans-serif; color: var(--ink); }

  .spread { position: relative; width: 1200px; height: 799px; }
  .page { position: absolute; top: 0; height: 799px; background: var(--paper); overflow: hidden; }
  .page--left { left: 0; width: 597px; }
  .page--right { left: 603px; width: 597px; }

  /* Left page */
  .cover-title {
    position: absolute; left: 50px; top: 36px;
    font-weight: 800; font-size: 31px; letter-spacing: 0.5px; color: var(--ts-blue);
  }
  .cover-script {
    position: absolute; left: 190px; top: 58px;
    font-family: "Great Vibes", cursive; font-size: 46px; color: var(--ts-green);
  }
  .cover-intro {
    position: absolute; left: 50px; top: 116px; width: 310px;
    font-size: 7.5px; line-height: 1.45; color: var(--ink);
  }
  .photo-plant {
    position: absolute; left: 38px; top: 170px; width: 300px; height: 390px;
    background:
      radial-gradient(ellipse 45% 35% at 55% 30%, #a8d85a 0%, #8cc63f 45%, rgba(140,198,63,0) 75%),
      radial-gradient(ellipse 60% 22% at 45% 78%, #d9a98a 0%, #c78f6c 50%, rgba(199,143,108,0) 80%),
      radial-gradient(ellipse 35% 12% at 55% 68%, #3a2a20 0%, rgba(58,42,32,0) 90%),
      #ffffff;
  }
  .brand {
    font-weight: 700; color: var(--ts-blue); letter-spacing: 2px; text-transform: uppercase;
  }
  .brand--cover { position: absolute; left: 236px; top: 590px; font-size: 20px; }
  .band { position: absolute; height: 10px; }
  .band--left { left: 0; width: 597px; top: 708px; background: var(--ts-green); }

  /* Right page */
  .photo-ducks {
    position: absolute; left: 178px; top: 0; width: 419px; height: 172px;
    background: linear-gradient(100deg, #fbf6e0 0%, #f6e27a 30%, #f2cf2c 60%, #f0c419 100%);
  }
  .brand--inside { position: absolute; left: 44px; top: 112px; font-size: 15px; }
  .vertical-script {
    position: absolute; left: 18px; top: 560px; transform-origin: left top; transform: rotate(-90deg);
    font-family: "Great Vibes", cursive; font-size: 44px; color: var(--ts-green); white-space: nowrap;
  }
  .photo-matches {
    position: absolute; left: 34px; top: 560px; width: 120px; height: 146px;
    background: linear-gradient(160deg, #ffffff 0%, #f3e3c8 35%, #e6cfa4 60%, #d63a2a 100%);
  }
  .content { position: absolute; left: 160px; top: 182px; width: 420px; }
  .section { margin-bottom: 7px; }
  .section-title { font-size: 8.5px; font-weight: 600; color: var(--ts-green-dark); text-transform: uppercase; margin-bottom: 2px; }
  .section p { font-size: 6.6px; line-height: 1.4; margin-bottom: 4px; }
  .value { margin-bottom: 4px; }
  .value-name { font-size: 6.8px; font-weight: 600; text-transform: uppercase; color: var(--ink); }
  .value p { margin: 0; }
  .band--right-blue { left: 0; width: 160px; top: 708px; background: var(--ts-blue-deep); }
  .band--right-green { left: 160px; width: 437px; top: 708px; background: var(--ts-green); }
</style>
</head>
<body>
<main class="spread">
  <section class="page page--left">
    <h1 class="cover-title">WE SEE THINGS</h1>
    <div class="cover-script">differently</div>
    <p class="cover-intro">Amber Fern Consult sees governance, strategy and risk at the heart of every decision. We believe that these disciplines are the roots of an organisation. Find out how we can help to embed a culture of governance, strategy and risk.</p>
    <div class="photo-plant" role="img" aria-label="Photograph of an open hand holding soil with a young green seedling"></div>
    <div class="brand brand--cover">Amber Fern</div>
    <div class="band band--left"></div>
  </section>

  <section class="page page--right">
    <div class="photo-ducks" role="img" aria-label="Photograph of a row of yellow rubber ducks with one facing the other way"></div>
    <div class="brand brand--inside">Amber Fern</div>
    <div class="vertical-script">make a difference</div>

    <div class="content">
      <div class="section">
        <h2 class="section-title">Service Pillars</h2>
        <p>Amber Fern operates within three broad service pillars: governance, strategy and risk. These are the underlying themes in all that we do, and in the skills of the advisors that we employ. Our service pillars represent the core commercial disciplines, each required in appropriate balance. Working across all sectors and several international boundaries ensures Amber Fern advisors are well-rounded in approach, and able to offer pragmatic guidance based on personal experience supported by access to a comprehensive global knowledge base.</p>
      </div>
      <div class="section">
        <h2 class="section-title">Practice Areas</h2>
        <p>Amber Fern operates across three practice areas: corporate advisory, professional conduct, and technology advisory. Each area has specialist advisors with deep domain expertise in their fields and a wealth of pragmatic commercial experience. Rigorous professional development is a continuing requirement, as is the maintenance of memberships for sharing best practice information.</p>
      </div>
      <div class="section">
        <h2 class="section-title">Tallyforge Suite</h2>
        <p>Amber Fern's Tallyforge Suite is used to simplify governance, bringing greater transparency and accountability to governance practice.</p>
      </div>
      <div class="section">
        <h2 class="section-title">Amber Fern Values</h2>
        <div class="value"><div class="value-name">Inspirational</div><p>in everything that we do and for everyone that we encounter</p></div>
        <div class="value"><div class="value-name">Courageous</div><p>in being independent, championing change, and acting with real integrity in the face of adversity</p></div>
        <div class="value"><div class="value-name">Leadership</div><p>as an intrinsic part of our culture that is collective, collaborative and compassionate</p></div>
        <div class="value"><div class="value-name">Pragmatic</div><p>in arriving at a deep understanding of our customers, their needs and measurable outcomes</p></div>
        <div class="value"><div class="value-name">Expertise</div><p>to actively meet key challenges in unique ways to achieve new possibilities</p></div>
      </div>
      <div class="section">
        <h2 class="section-title">In the Community</h2>
        <p>Amber Fern is committed to acting as a responsible corporate citizen, and we strive to improve the quality of life for those around us through financial contributions, in-kind donations and staff volunteering.</p>
        <p>Our community giving activities are based on a philosophy of spreading globally and giving back locally. We are not bounded by geography, and support community initiatives on our doorstep and in every corner of the world.</p>
        <p>Our support for the community is giving to engage, combining both financial and volunteer support. We encourage our staff and business partners to get involved in both local and remote communities, and to support programs that are making a positive difference to people's lives.</p>
      </div>
    </div>

    <div class="photo-matches" role="img" aria-label="Photograph of a bundle of red-tipped matches with one burnt match"></div>
    <div class="band band--right-blue"></div>
    <div class="band band--right-green"></div>
  </section>
</main>
</body>
</html>
```